web page layout, style , color, font & flow design

We are developing a single page application. The SPA (single page application) will display natural gas pipeline flow data once the customer logs on. The customer has a choice of the region, the pipeline, the zone on the pipeline, whether the point is a delivery point or receipt point and the state the pipeline flows through.
we have jumpstarted the project and are attaching a pdf of the same.

we are using mockingbird for the wireframe. any designer is free to use this tool to make changes.

A mockingbird wireframe link is added below. you are free to use it and to make changes. please save the changed wireframe in a different name

we are looking for inputs on layout, style , color, font & flow.

A logo jpg file has also been attached.

Target Market(s)

this single web page is going to be used by natural gas traders and schedulers day in and day out. the application is more of business to business corporate application.

Industry/Entity Type

Delivery

Requirements
Must have
• layout ,flow, size, color, font , ease of use.

```html
<!DOCTYPE html>
<html lang="en">
<head>
<meta charset="utf-8">
<title>Flowline – Pipeline Flow Data</title>
<link href="https://fonts.googleapis.com/css2?family=Ubuntu:wght@400;500&display=swap" rel="stylesheet">
<style>
:root{
  --black:#000;
  --side:#5f5f5f;
  --side-line:#6e6e6e;
  --side-active:#3b3b3b;
  --side-text:#e4e4e4;
  --main-bg:#e8e8e8;
  --panel:#fff;
  --head-dark:#404040;
  --table-head:#d2d0d0;
  --row-alt:#ede8e8;
  --text:#444;
  --muted:#666;
  --green:#7cb52f;
  --orange:#f26a21;
  --blue:#0053a0;
  --pink:#ec1c6b;
  --cyan:#1aa5e0;
  --purple:#9b49b4;
  --accent:#139be0;
}
*{box-sizing:border-box;margin:0;padding:0}
html,body{width:1200px;height:938px;overflow:hidden}
body{font-family:"Ubuntu",sans-serif;color:var(--text);background:var(--main-bg);position:relative}

.sidebar{position:absolute;left:0;top:0;width:219px;height:938px;background:var(--side)}
.brand{height:154px;background:var(--black);position:relative;display:flex;align-items:center;justify-content:center;gap:10px}
.brand::after{content:"";position:absolute;left:94px;bottom:-12px;border:12px solid transparent;border-bottom:0;border-top-color:var(--black)}
.brand-dot{width:22px;height:22px;border-radius:50%;background:var(--green)}
.brand-name{color:#fff;font-size:26px;font-weight:500}
.pipelines{list-style:none;margin-top:16px;border-top:1px solid var(--side-line)}
.pipelines li{height:33px;line-height:32px;padding-left:17px;font-size:12.5px;color:var(--side-text);border-bottom:1px solid var(--side-line);position:relative;white-space:nowrap}
.pipelines li.active{background:var(--side-active);color:#fff}
.pipelines .tick{position:absolute;right:10px;top:7px;width:19px;height:19px;background:var(--green)}

.regions{position:absolute;left:219px;top:0;right:0;height:38px;background:#fff;display:flex}
.regions a{width:127.5px;height:38px;line-height:38px;text-align:center;color:#fff;font-size:12.5px;text-decoration:none;border-right:1px solid #fff}
.r-ne{background:var(--green)}.r-mw{background:var(--orange)}.r-se{background:var(--blue)}
.r-sw{background:var(--pink)}.r-c{background:var(--cyan)}.r-w{background:var(--purple)}
.add{margin:7px 0 0 10px}
.social{position:absolute;right:8px;top:10px;display:flex;gap:12px}
.social span{width:17px;height:17px;border-radius:50%;background:#7a7a7a}

.filter{position:absolute;left:238px;top:58px;width:941px;height:197px;background:var(--panel)}
.filter-head{height:37px;background:var(--head-dark);color:#fff;font-size:22px;line-height:37px;padding-left:21px;position:relative}
.filter-head .toggle{position:absolute;right:11px;top:9px}
.fields{display:flex;padding:31px 0 0 25px;height:110px;border-bottom:1px solid #e2e2e2}
.field{width:317px}
.select{width:230px;height:28px;border:1px solid #c9c9c9;background:#ececec;position:relative;font-size:12.5px;line-height:26px;padding-left:10px;color:#333}
.select::after{content:"";position:absolute;right:0;top:0;width:32px;height:26px;border-left:1px solid #c9c9c9;background:#ececec}
.select::before{content:"";position:absolute;right:10px;top:11px;border:6px solid transparent;border-top:6px solid #8a8a8a;z-index:1}
.hint{font-size:10px;color:var(--muted);margin-top:11px;padding-left:2px}
.search{position:absolute;left:358px;top:157px;width:190px;height:32px;background:var(--accent);color:#fff;border:0;font:14px "Ubuntu",sans-serif;border-radius:2px}

.flows{position:absolute;left:238px;top:283px;width:941px;table-layout:fixed;border-collapse:collapse;background:#fff;font-size:11px;border:1px solid #ddd}
.flows th{height:37px;background:var(--table-head);font-weight:400;font-size:12.5px;text-align:left;color:#333;padding-left:28px;white-space:nowrap}
.flows td{height:33px;padding-left:32px;color:#444;white-space:nowrap;overflow:hidden}
.flows tbody tr:nth-child(even) td{background:var(--row-alt)}

.pager{position:absolute;right:21px;top:665px;display:flex;border:1px solid #ddd;background:#fff;font-size:12px;height:27px}
.pager span{padding:0 10px;line-height:26px;border-right:1px solid #ddd;color:#333}
.pager .current{background:var(--accent);color:#fff;border-color:var(--accent)}
.pager .disabled{color:#aaa;border:0}

.footer{position:absolute;left:219px;right:0;top:885px;height:53px;background:#f5f5f5;display:flex;align-items:center;padding-left:16px;font-size:11.5px;color:#555}
.footer-brand{display:flex;align-items:center;gap:5px;margin-right:18px;color:#333;font-size:13px;font-weight:500}
.footer-brand i{width:12px;height:12px;border-radius:50%;background:var(--green)}
.footer .social{top:18px;right:14px}
</style>
</head>
<body>
<aside class="sidebar">
  <div class="brand"><span class="brand-dot"></span><span class="brand-name">Flowline</span></div>
  <ul class="pipelines">
    <li>Alder Ridge</li><li>CRT</li>
    <li class="active">Dunmore<span class="tick"><svg width="19" height="19" viewBox="0 0 19 19"><path d="M5 10l3 3 6-7" fill="none" stroke="#fff" stroke-width="2"/></svg></span></li>
    <li>Eastbank NG</li><li>East Valley NG</li><li>Emberline Gas</li><li>Equiline Inc</li>
    <li>Graniteview Gas</li><li>Ironwood</li><li>Harborline &amp; North East</li><li>Meridian Pipeline</li>
    <li>Northfield Fuel Gas Supply Corp</li><li>Portview NG</li><li>St. Lucas Gas</li><li>Tenwood Gas</li>
    <li>Tecora</li><li>Transvale</li>
  </ul>
</aside>

<nav class="regions">
  <a class="r-ne">North East</a><a class="r-mw">MidWest</a><a class="r-se">SouthEast</a>
  <a class="r-sw">SouthWest</a><a class="r-c">Central</a><a class="r-w">West</a>
  <svg class="add" width="24" height="24" viewBox="0 0 24 24"><circle cx="12" cy="12" r="11" fill="none" stroke="#777" stroke-width="1.5"/><path d="M12 6v12M6 12h12" stroke="#777" stroke-width="2"/></svg>
  <div class="social"><span></span><span></span><span></span></div>
</nav>

<section class="filter">
  <div class="filter-head">Filter
    <svg class="toggle" width="20" height="20" viewBox="0 0 20 20"><circle cx="10" cy="10" r="10" fill="#fff"/><rect x="5" y="9" width="10" height="2.5" fill="#404040"/></svg>
  </div>
  <div class="fields">
    <div class="field"><div class="select">-- Location Type --</div><p class="hint">Eg. Receipt,Delivery,Storage</p></div>
    <div class="field"><div class="select">-- States --</div><p class="hint">Eg. Interstate pipeline</p></div>
    <div class="field"><div class="select">-- Zones --</div><p class="hint">Eg. pipeline zones</p></div>
  </div>
  <button class="search">Search</button>
</section>

<table class="flows">
  <colgroup><col style="width:121px"><col style="width:101px"><col style="width:135px"><col style="width:102px"><col style="width:135px"><col style="width:101px"><col style="width:101px"><col></colgroup>
  <thead><tr><th>Gasday</th><th>Location</th><th>Loc_Name</th><th>Flow_Ind</th><th>Loc_Desc</th><th>Op_cap</th><th>Sch_cap</th><th>Op_avail_cap</th></tr></thead>
  <tbody>
  <tr><td>Item 3</td><td>Item 4</td><td>Location name 1</td><td>test 1</td><td>Lorem ipsum dolor…</td><td>test 1</td><td>test 1</td><td>test 1</td></tr>
  <tr><td>Item 5</td><td>Item 6</td><td>Location name 2</td><td>test 2</td><td>Lorem ipsum dolor…</td><td>test 2</td><td>test 2</td><td>test 2</td></tr>
  <tr><td>Item 7</td><td>Item 8</td><td>Location name 3</td><td>test 1</td><td>Lorem ipsum dolor…</td><td>test 1</td><td>test 1</td><td>test 1</td></tr>
  <tr><td>Item 9</td><td>Item 10</td><td>Location name 4</td><td>test 2</td><td>Lorem ipsum dolor…</td><td>test 2</td><td>test 2</td><td>test 2</td></tr>
  <tr><td>Item 11</td><td>Item 12</td><td>Location name 5</td><td>test 1</td><td>Lorem ipsum dolor…</td><td>test 1</td><td>test 1</td><td>test 1</td></tr>
  <tr><td>Item 13</td><td>Item 14</td><td>Location name 6</td><td>test 2</td><td>Lorem ipsum dolor…</td><td>test 2</td><td>test 2</td><td>test 2</td></tr>
  <tr><td>Item 15</td><td>Item 16</td><td>Location name 7</td><td>test 1</td><td>Lorem ipsum dolor…</td><td>test 1</td><td>test 1</td><td>test 1</td></tr>
  <tr><td>Item 17</td><td>Item 18</td><td>Location name 8</td><td>test 2</td><td>Lorem ipsum dolor…</td><td>test 2</td><td>test 2</td><td>test 2</td></tr>
  <tr><td>Item 19</td><td>Item 20</td><td>Location name 9</td><td>test 1</td><td>Lorem ipsum dolor…</td><td>test 1</td><td>test 1</td><td>test 1</td></tr>
  <tr><td>Item 21</td><td>Item 22</td><td>Location name 10</td><td>test 2</td><td>Lorem ipsum dolor…</td><td>test 2</td><td>test 2</td><td>test 2</td></tr>
  </tbody>
</table>

<div class="pager"><span>← Previous</span><span>1</span><span class="current">2</span><span class="disabled">Next →</span></div>

<footer class="footer">
  <div class="footer-brand"><i></i>Flowline</div>
  Copyright © Flowline 2014. All Rights Reserved
  <div class="social"><span></span><span></span><span></span></div>
</footer>
</body>
</html>
```